Very high end short term vacation rentals.

Amber Tide Harbor Estates. Design business cards using existing logo. Should represent high quality, class accommodations. The back side will have a QR code linking to website/video and pictures

```html
<!DOCTYPE html>
<html lang="en">
<head>
<meta charset="utf-8">
<title>Amber Tide Harbor Estates — Business Cards</title>
<link href="https://fonts.googleapis.com/css2?family=Cinzel:wght@400;500&family=Arimo:wght@400&display=swap" rel="stylesheet">
<style>
  :root {
    --stage: #1c1c1d;
    --card: #0b0b0b;
    --ink: #f4f4f4;
    --ink-soft: #cfcfcf;
    --rule: #5a5a5a;
  }
  * { box-sizing: border-box; margin: 0; padding: 0; }
  html, body { width: 1200px; height: 900px; overflow: hidden; background: var(--stage); }
  .stage {
    width: 1200px; height: 900px;
    display: flex; align-items: center; justify-content: center; gap: 40px;
  }
  .card {
    position: relative;
    width: 540px; height: 310px;
    background: var(--card);
    border-radius: 20px;
    color: var(--ink);
    overflow: hidden;
  }
  /* Front: brand + contact */
  .brand-ring {
    position: absolute; left: 62px; top: 40px;
    width: 150px; height: 150px;
    border: 3px solid var(--ink); border-radius: 50%;
  }
  .brand-name {
    position: absolute; left: 16px; top: 204px; width: 244px;
    font-family: "Cinzel", serif; font-weight: 400;
    font-size: 23px; line-height: 1.2; text-align: center;
    color: var(--ink); letter-spacing: 0.5px;
  }
  .divider {
    position: absolute; left: 272px; top: 48px;
    width: 1px; height: 200px; background: var(--rule);
  }
  .contact {
    position: absolute; left: 296px; top: 44px; right: 16px;
  }
  .person-name {
    font-family: "Cinzel", serif; font-weight: 500;
    font-size: 21px; letter-spacing: 0.5px; line-height: 1.05;
  }
  .person-role {
    font-family: "Arimo", sans-serif; font-size: 14px; color: var(--ink-soft);
    margin-bottom: 16px;
  }
  .contact-list { list-style: none; font-family: "Arimo", sans-serif; font-size: 14px; }
  .contact-list li { display: flex; align-items: center; gap: 8px; height: 23px; }
  .contact-list svg { width: 14px; height: 14px; flex: none; }
  .address {
    font-family: "Arimo", sans-serif; font-size: 14px; line-height: 1.4;
    margin-top: 12px; padding-left: 22px;
  }
  /* Back: brand mark + name, centred as a group */
  .card--back {
    display: flex; align-items: center; justify-content: center; gap: 28px;
  }
  .back-ring {
    width: 130px; height: 130px; flex: none;
    border: 3px solid var(--ink); border-radius: 50%;
  }
  .back-name {
    font-family: "Cinzel", serif; font-weight: 400;
    font-size: 28px; line-height: 1.15; color: var(--ink); letter-spacing: 0.5px;
  }
</style>
</head>
<body>
  <main class="stage">
    <section class="card card--front" aria-label="Business card front">
      <div class="brand-ring"></div>
      <div class="brand-name">Amber Tide<br>Harbor Estates</div>
      <div class="divider"></div>
      <div class="contact">
        <div class="person-name">Marcus Hale</div>
        <div class="person-role">Managing Director</div>
        <ul class="contact-list">
          <li>
            <svg viewBox="0 0 16 16" aria-hidden="true"><path d="M4 1.5l2.2 3-1.4 1.6c.8 1.9 2.2 3.3 4.1 4.1l1.6-1.4 3 2.2-1.2 2.6C7 13.6 2.4 9 1.4 2.7z" fill="var(--ink)"/></svg>
            044-555 201 347
          </li>
          <li>
            <svg viewBox="0 0 16 16" aria-hidden="true"><rect x="1" y="3" width="14" height="10" fill="var(--ink)"/><path d="M1 3l7 6 7-6" fill="none" stroke="var(--card)" stroke-width="1.4"/></svg>
            info@ambertide.com
          </li>
          <li>
            <svg viewBox="0 0 16 16" aria-hidden="true"><circle cx="8" cy="8" r="6.5" fill="none" stroke="var(--ink)" stroke-width="1.5"/><ellipse cx="8" cy="8" rx="2.8" ry="6.5" fill="none" stroke="var(--ink)" stroke-width="1.2"/><path d="M1.5 8h13" stroke="var(--ink)" stroke-width="1.2"/></svg>
            www.ambertideestates.com
          </li>
        </ul>
        <p class="address">88 Harbor Lane, Suite 4<br>40217, Isla Verde</p>
      </div>
    </section>

    <section class="card card--back" aria-label="Business card back">
      <div class="back-ring"></div>
      <div class="back-name">Amber Tide<br>Harbor Estates</div>
    </section>
  </main>
</body>
</html>
```